Flyer for an online formula one racing league

Hello.

I am looking for the perfect one page facebook/instagram style flyer for an online formula one racing league. The racing league is called 'VOLTA RACING LEAGUE'.

Information that MUST be on the new flyer is already on the old flyer I have uploaded here. In addition to including: The Volta racing league 'V' logo I have uploaded AND the text: 'Very popular, clean and competitive racing league, running for its 4th season. Why not join with a friend? Race times, Mondays, Tuesdays and Wednesdays each at 8pm UK TIME Message below for any questions. (Spacing of information is not important, however all the information in regards to the racing I have just mentioned MUST BE on the flyer, this includes info from old pic, logo and the other info I just mentioned).

It would be beneficial to have lots of dark blue on the flyer and the new flyer to be a lot different to the original flyer I uploaded, but this is not essential.

I apologise if I did not explain very well, any questions, please message me.

The best flyer should look the most attractive to someone that might be interested in joining an online formula one racing league.

I used this website before to create the perfect logo for my Sunday League team last year, and I was very impressed. I look forward to seeing your submissions.

Target Market(s)

No specific target, more something that may attract someone into joining a formula one online racing league

Industry/Entity Type

e sports/formula one

Colors
0054AA
0677BA
7BADD7
CADEEF
E8F1F8

Requirements
Must have
• Read product description please
Should not have
• Ignoring product description!

```html
<!DOCTYPE html>
<html lang="en">
<head>
<meta charset="utf-8">
<title>Volta Racing League – Season 4 Flyer</title>
<link rel="stylesheet" href="https://fonts.googleapis.com/css2?family=Bebas+Neue&family=Montserrat:wght@700&display=swap">
<style>
  :root {
    --navy: #1b1a5c;
    --navy-deep: #141449;
    --race-blue: #0b3b9f;
    --race-blue-light: #1450b8;
    --yellow: #ffc60a;
    --grey: #b9b8cf;
    --white: #ffffff;
    --badge: #0d1233;
  }
  * { margin: 0; padding: 0; box-sizing: border-box; }
  html, body {
    width: 1200px; height: 628px; overflow: hidden;
    background: var(--navy);
  }
  .flyer {
    position: relative; width: 1200px; height: 628px; overflow: hidden;
    font-family: "Bebas Neue", "Oswald", sans-serif;
    color: var(--white);
  }
  .header-band {
    position: absolute; left: 0; top: 0; width: 1200px; height: 292px;
    background: var(--navy);
  }
  .league-badge {
    position: absolute; top: 24px; width: 136px; height: 136px;
    border-radius: 50%; background: var(--badge);
    display: flex; align-items: center; justify-content: center;
    font-size: 96px; line-height: 1; color: var(--white);
    padding-top: 8px;
  }
  .league-badge--left { left: 37px; }
  .league-badge--right { left: 1027px; }
  .league-title {
    position: absolute; left: 0; top: 30px; width: 1200px;
    text-align: center; font-size: 104px; line-height: 1;
    color: var(--yellow); letter-spacing: 1px; font-weight: 400;
  }
  .league-tagline {
    position: absolute; left: 0; top: 168px; width: 1200px;
    text-align: center; font-size: 40px; line-height: 49px;
    color: var(--grey); letter-spacing: 0.5px;
  }
  .schedule-band {
    position: absolute; left: 0; top: 292px; width: 1200px; height: 238px;
    background: linear-gradient(90deg, var(--race-blue) 0%, var(--race-blue-light) 50%, var(--race-blue) 100%);
  }
  .schedule-backdrop {
    position: absolute; inset: 0;
    background: radial-gradient(ellipse 60% 70% at 55% 75%, rgba(255,255,255,0.07), rgba(255,255,255,0) 70%);
  }
  .schedule-text {
    position: relative; padding-top: 20px;
    text-align: center; font-size: 74px; line-height: 66px;
    letter-spacing: 0.5px;
  }
  .footer-band {
    position: absolute; left: 0; top: 530px; width: 1200px; height: 98px;
    background: var(--navy);
  }
  .footer-invite {
    position: absolute; left: 35px; top: 27px;
    font-size: 50px; line-height: 1; color: var(--yellow);
  }
  .footer-contact {
    position: absolute; left: 617px; top: 44px;
    font-family: "Montserrat", sans-serif; font-weight: 700;
    font-size: 17px; line-height: 1; letter-spacing: 2.2px;
    color: var(--white);
  }
</style>
</head>
<body>
  <main class="flyer">
    <section class="header-band">
      <div class="league-badge league-badge--left">V</div>
      <div class="league-badge league-badge--right">V</div>
      <h1 class="league-title">VOLTA RACING LEAGUE</h1>
      <p class="league-tagline">VERY POPULAR, CLEAN AND COMPETITIVE RACING LEAGUE<br>RUNNING FOR ITS 4TH SEASON!</p>
    </section>

    <section class="schedule-band">
      <div class="schedule-backdrop" role="img" aria-label="Faint photo of a formula one racing car on track"></div>
      <p class="schedule-text">RACING TIMES:<br>MONDAYS, TUESDAYS AND WEDNESDAYS<br>EACH AT 8PM UK TIME</p>
    </section>

    <section class="footer-band">
      <p class="footer-invite">WHY NOT JOIN WITH A FRIEND?</p>
      <p class="footer-contact">MESSAGE BELOW FOR ANY QUESTIONS</p>
    </section>
  </main>
</body>
</html>
```